Business Card and Letterhead for Vantage Psychology

We need a business card design and letterhead to use for our Psychology firm that specializes in psychoeducational assessments and individual therapy. Our motto is Purpose-Driven Assessments, Meaning-Centered Therapy.Our contact information is as follows:
Vantage Psychology
The Marwick Block - 6127-48St.
Box 2716 Olds, AB
T2K 3M8
t 403.555.0148 (VANT)
f 403.555.0172
www.vantagepsychology-example.ca
The business card will be used for two different psychologists so I can supply names nearer to completion. We prefer clean, uncluttered looks.

Target Market(s)

Clients, Educators

Font styles to use
Sans Serif

Colors

Designer to choose colors to be used in the design.

Requirements
Must have
• All relevant contact info, logo, some "white" space.
Nice to have
• It would be nice to see letterhead options that have the logo on the top of the page but also options that have it on the side. I think top of the page is probably our preference.
Should not have
• Too much clutter!

```html
<!DOCTYPE html>
<html lang="en">
<head>
<meta charset="utf-8">
<title>Vantage Psychology – Business Card</title>
<link rel="stylesheet" href="https://fonts.googleapis.com/css2?family=Roboto:wght@300;400;500&display=swap">
<style>
  :root {
    --backdrop: #3a3a3a;
    --card: #ffffff;
    --ink: #111111;
    --orange: #f1a84a;
    --blue: #56bedb;
    --shadow: rgba(0, 0, 0, 0.45);
  }
  * { box-sizing: border-box; margin: 0; padding: 0; }
  html, body {
    width: 1200px;
    height: 686px;
    overflow: hidden;
    background: var(--backdrop);
    font-family: "Roboto", Arial, sans-serif;
  }
  .stage { position: relative; width: 1200px; height: 686px; }
  .card {
    position: absolute;
    background: var(--card);
    box-shadow: -14px 10px 30px var(--shadow);
  }
  .card--front { left: 74px; top: 162px; width: 507px; height: 342px; }
  .card--back  { left: 627px; top: 159px; width: 506px; height: 339px; }

  .name-frame {
    position: absolute;
    left: 71px; top: 95px;
    width: 360px; height: 55px;
    border: 2px solid var(--orange);
    display: flex; align-items: center; justify-content: center;
  }
  .name {
    font-weight: 500;
    font-size: 41px;
    color: var(--ink);
    letter-spacing: 0.2px;
    line-height: 1;
  }
  .role {
    position: absolute;
    left: 186px; top: 157px;
    font-weight: 400;
    font-size: 18px;
    letter-spacing: 3px;
    color: var(--blue);
  }
  .address {
    position: absolute;
    left: 36px; top: 228px;
    font-style: normal;
    font-weight: 400;
    font-size: 14px;
    line-height: 18px;
    letter-spacing: 1px;
    color: var(--ink);
  }
  .address span { display: block; }
  .address span + span { padding-left: 2px; }
  .phones {
    position: absolute;
    right: 28px; top: 228px;
    font-size: 14px;
    letter-spacing: 1px;
    color: var(--ink);
    text-align: right;
    line-height: 18px;
  }
  .phones span { display: block; }
  .phones span + span { margin-top: 16px; }
  .band {
    position: absolute;
    left: 0; bottom: 0;
    width: 100%; height: 36px;
    display: flex;
  }
  .band__orange { width: 252px; background: var(--orange); }
  .band__blue { flex: 1; background: var(--blue); }

  .brand-dot {
    position: absolute;
    left: 201px; top: 93px;
    width: 120px; height: 120px;
    border-radius: 50%;
    background: var(--blue);
  }
  .brand-name {
    position: absolute;
    left: 0; top: 216px;
    width: 100%;
    text-align: center;
    font-weight: 500;
    font-size: 30px;
    letter-spacing: 1.5px;
    color: var(--blue);
  }
  .website {
    position: absolute;
    left: 0; top: 268px;
    width: 100%;
    text-align: center;
    font-size: 18px;
    color: var(--ink);
  }
</style>
</head>
<body>
<main class="stage">
  <section class="card card--front" aria-label="Business card front">
    <div class="name-frame"><h1 class="name">YOUR NAME HERE</h1></div>
    <p class="role">PSYCHOLOGIST</p>
    <address class="address">
      <span>The Marwick Block -6127-48St.</span>
      <span>Box 2716 Olds, AB</span>
      <span>T2K 3M8</span>
    </address>
    <p class="phones">
      <span>403.555.0148</span>
      <span>403.555.0172</span>
    </p>
    <div class="band"><div class="band__orange"></div><div class="band__blue"></div></div>
  </section>

  <section class="card card--back" aria-label="Business card back">
    <div class="brand-dot"></div>
    <h2 class="brand-name">VANTAGE PSYCHOLOGY</h2>
    <p class="website">www.vantagepsychology-example.ca</p>
  </section>
</main>
</body>
</html>
```